CEO of company needs clear business card that stands out from the rest

I need a clear business card (standard credit card size) for the CEO/Founder of our company...Brightfield Counseling. We would like to see designs that use our logo colors, which are khaki, chocolate brown, and gray. The card should be an edgy design, maybe where half the card is transparent with curves on the card, or a textured card where the logo is transparent, I don't care much for white cards. The final design should communicate a funky, edgy, and modern look, as well as stand out to have the "WOW" factor. The information we need on the card would be Name, Title, Toll free number, Phone Number, address, email address, and website.

*PLEASE SEND FRONT AND BACK OF CARDS

Card is two sided front and back please give us your front and back designs

The card should be an edgy design, maybe where half the card is transparent with curves on the card, or a textured card where the logo is transparent, I don't care much for white cards. The final design should communicate a funky, edgy, and modern look, as well as stand out to have the "WOW" factor.

Please follow these guidelines for the card

SPECS (card):

2.125 (h) x 3.375 (w) card size after cut

2.375 (h) x 3.625 (w) card with bleed

300 dpi

cmyk

1/8 bleed

allow 1/8 border for live area

I will also attached the pdf for the information listed above which includes a diagram of the card

 

All the cards need to have rounded edges

I just updated a card as an example of how you can use different fonts on a single business card, look how the name is written in script, so what I am saying is make this a card you will be proud to design and put it in your portfolio 

Reason: this race is really close and I am working with 2 designers to fine tune their designs and the weekend is slowing us down

• Our Logo
MUST HAVE PARTS OF CARD THAT ARE TRANSPARENT. See ideas that are attached.
Card is two sided front and back
• The final design should communicate a funky, edgy, and modern look, as well as stand out to have the "WOW" factor. The information we need on the card would be Name, Title, Toll free number, Phone Number, address, email address, and website.

```html
<!DOCTYPE html>
<html lang="en">
<head>
<meta charset="utf-8">
<title>Brightfield Counseling – Business Card</title>
<link rel="stylesheet" href="https://fonts.googleapis.com/css2?family=Arimo:wght@400;700&display=swap">
<style>
  :root {
    --stage: #3a3a3a;
    --panel: #d4d6d7;
    --chocolate: #4a2614;
    --chocolate-deep: #2e160b;
    --khaki: #b06a2c;
    --gray: #8d8d8d;
    --clear: rgba(225, 228, 230, 0.22);
    --clear-edge: rgba(255, 255, 255, 0.35);
    --ink-light: #ffffff;
    --ink-soft: #d9c9bd;
  }
  * { box-sizing: border-box; margin: 0; padding: 0; }
  html, body { width: 1200px; height: 886px; overflow: hidden; }
  body {
    background: var(--stage);
    font-family: "Arimo", Arial, sans-serif;
    position: relative;
  }
  .brand-panel {
    position: absolute;
    left: 0; top: 36px;
    width: 685px; height: 274px;
    background: var(--panel);
    display: flex;
    align-items: center;
    justify-content: center;
    gap: 22px;
  }
  .brand-dot {
    width: 46px; height: 46px;
    border-radius: 50%;
    background: var(--khaki);
  }
  .brand-name {
    font-size: 54px;
    font-weight: 400;
    color: var(--chocolate);
    letter-spacing: -0.5px;
  }
  .card {
    position: absolute;
    top: 440px;
    width: 500px; height: 315px;
    border-radius: 18px;
    overflow: hidden;
    background: var(--clear);
    border: 1px solid var(--clear-edge);
    box-shadow: 0 10px 24px rgba(0,0,0,0.45);
  }
  .card-front { left: 60px; }
  .card-back { left: 640px; }
  .card-shape { position: absolute; inset: 0; width: 100%; height: 100%; }
  .holder {
    position: absolute;
    left: 34px; top: 92px;
    color: var(--ink-light);
  }
  .holder-name { font-size: 30px; font-weight: 700; }
  .holder-title { font-size: 13px; color: var(--ink-soft); margin-top: 4px; }
  .contact {
    position: absolute;
    left: 34px; bottom: 26px;
    list-style: none;
    font-size: 11.5px;
    line-height: 16px;
    color: var(--ink-soft);
  }
  .back-brand {
    position: absolute;
    left: 190px; top: 120px;
    display: flex;
    align-items: center;
    gap: 12px;
  }
  .back-brand .brand-dot { width: 26px; height: 26px; }
  .back-brand .brand-name { font-size: 26px; color: var(--panel); }
</style>
</head>
<body>
  <header class="brand-panel">
    <span class="brand-dot"></span>
    <span class="brand-name">Brightfield Counseling</span>
  </header>

  <section class="card card-front">
    <svg class="card-shape" viewBox="0 0 500 315" preserveAspectRatio="none" aria-hidden="true">
      <defs>
        <linearGradient id="front-fill" x1="0" y1="0" x2="1" y2="1">
          <stop offset="0" stop-color="#4a2614"/>
          <stop offset="1" stop-color="#2e160b"/>
        </linearGradient>
      </defs>
      <path d="M0,75 C120,60 200,30 260,0 L330,0 C395,10 405,70 362,122 C322,172 312,250 342,315 L0,315 Z" fill="url(#front-fill)"/>
    </svg>
    <div class="holder">
      <div class="holder-name">Dalton Whitaker</div>
      <div class="holder-title">Founder / CEO</div>
    </div>
    <ul class="contact">
      <li>f. 555.214.7260</li>
      <li>t. 555.308.4440</li>
      <li>dwhitaker@brightfieldcounseling.com</li>
      <li>4180 Linden Crest Dr. N.W. Suite 210</li>
      <li>Millbrook GA 30990</li>
      <li>www.brightfieldcounseling.com</li>
      <li>toll free #: 1.855.555.0182</li>
    </ul>
  </section>

  <section class="card card-back">
    <svg class="card-shape" viewBox="0 0 500 315" preserveAspectRatio="none" aria-hidden="true">
      <defs>
        <linearGradient id="back-fill" x1="0" y1="0" x2="1" y2="1">
          <stop offset="0" stop-color="#4a2614"/>
          <stop offset="1" stop-color="#2e160b"/>
        </linearGradient>
      </defs>
      <path d="M120,0 L500,0 L500,315 L330,315 C280,250 200,240 120,250 C60,256 22,228 60,170 C100,110 62,40 120,0 Z" fill="url(#back-fill)"/>
    </svg>
    <div class="back-brand">
      <span class="brand-dot"></span>
      <span class="brand-name">Brightfield Counseling</span>
    </div>
  </section>
</body>
</html>
```